Luxury Real Estate Website, Midwest, United States

We need web design services for a luxury website. We need IDX Integration with our MLS. We want this to be a very simple website with amazing graphics. We want it to link up with our MailChimp account in order to generate leads through a "More Information" Pop up on the main page. We want the main page to be covered with one large graphic that is a rolling slideshow of active listings of $400,000 and up from the IDX Integration. We need this website to give a very exclusive and sleek look. Lots of black is good... I will upload our logos in Black and Silver. We will also need an "About" page that we are going to call "MyQV Info". We want our graphics to be extremely impressive. Keep in mind, we are a company in the Midwest of the United States, and our real estate has a different look than homes in California or Florida. We need graphics that are realistic for the Midwest, yet still high-end.
Target Market(s)
Luxury Homeowners in the Midwest United States. The graphics needs to be pristine.
Industry/Entity Type
Real Estate
Coding
Coded - Design and coding required
Number of Pages Required
3 page
Requirements
Must have
- Large graphics with IDX Integration. The photos of real estate need to represent real estate that is common in the Midwest, United States. We also need MailChimp integration. We need a pop up that is titled "My Free Market Analysis" that makes them fill out a contact form asking for Full Name, Email Address, Phone Number and Address. This needs to be a pop up on the front page and will integrate with our MailChimp account. We also need a page called "About My QV Home". And another page where clients can download informational PDFs. The main component needs to be a front page search engine connected with the IDX to access active listings from our MLS. I attached our logos and a sample front page of a website. I would love for ours to look similar.
Nice to have
- Lake House photos on midwest lakes are a plus.
Should not have
- Should not have clutter. This website needs to be clean, luxurious and exclusive.

```html
<!DOCTYPE html>
<html lang="en">
<head>
<meta charset="utf-8">
<title>My QV Home — My Free Market Analysis</title>
<link href="https://fonts.googleapis.com/css2?family=Lato:ital,wght@0,300;0,400;0,700;1,400&display=swap" rel="stylesheet">
<style>
  :root {
    --navy-deep: #121726;
    --navy-panel: #161c2c;
    --line-soft: rgba(255, 255, 255, 0.35);
    --text-white: #ffffff;
    --text-muted: #c9ccd4;
    --field-bg: #ffffff;
    --field-placeholder: #b5b8bf;
    --button-grey: #8a8d94;
    --hero-sky: #8e9bab;
    --hero-mid: #5d7a45;
    --hero-ground: #4a6d2c;
  }
  * { box-sizing: border-box; margin: 0; padding: 0; }
  html, body {
    width: 1200px; height: 570px; overflow: hidden;
    background: var(--navy-deep);
    font-family: "Lato", Arial, sans-serif;
  }
  .canvas { position: relative; width: 1200px; height: 570px; overflow: hidden; }

  /* ---------- site behind the pop-up ---------- */
  .site { position: absolute; inset: 0; filter: blur(5px); }
  .hero-photo {
    position: absolute; left: 0; top: 0; width: 870px; height: 570px;
    background: linear-gradient(180deg, var(--hero-sky) 0%, var(--hero-mid) 45%, var(--hero-ground) 100%);
  }
  .hero-dots { position: absolute; top: 22px; left: 400px; display: flex; gap: 36px; }
  .hero-dots span { width: 14px; height: 14px; border-radius: 50%; background: rgba(255,255,255,0.75); }
  .hero-dots span.is-active { background: #fff; }

  .listing-search {
    position: absolute; left: 262px; top: 445px; width: 386px; height: 140px;
    background: rgba(22, 28, 44, 0.9); padding: 30px 18px 0;
  }
  .listing-search__bar { height: 18px; background: rgba(255,255,255,0.85); }
  .listing-search__link { margin-top: 14px; text-align: right; font-size: 9px; color: var(--text-muted); }

  .side-panel {
    position: absolute; left: 870px; top: 0; width: 330px; height: 570px;
    background: var(--navy-panel); color: var(--text-muted);
  }
  .brand {
    position: absolute; top: 142px; left: 0; width: 100%; text-align: center;
    font-weight: 300; font-size: 30px; letter-spacing: 3px; color: var(--text-muted);
  }
  .main-nav {
    position: absolute; left: 42px; top: 245px; width: 258px; height: 186px;
    border: 1px solid var(--line-soft); list-style: none;
    display: flex; flex-direction: column; justify-content: center; align-items: center; gap: 22px;
    font-size: 13px; letter-spacing: 1.5px;
  }
  .site-footer {
    position: absolute; left: 0; top: 510px; width: 100%; text-align: center;
    font-size: 8px; letter-spacing: 1px; line-height: 12px;
  }

  .dim { position: absolute; inset: 0; background: rgba(10, 12, 20, 0.25); }

  /* ---------- pop-up ---------- */
  .analysis-popup {
    position: absolute; left: 399px; top: 102px; width: 404px; height: 351px;
    background: var(--navy-deep); color: var(--text-white); text-align: center;
  }
  .analysis-popup__close { position: absolute; left: 369px; top: 15px; width: 20px; height: 20px; }
  .analysis-popup__title {
    margin-top: 44px; font-weight: 300; font-size: 23px; letter-spacing: 0.5px;
  }
  .analysis-popup__intro {
    margin: 12px auto 0; width: 250px; font-weight: 300; font-size: 13.5px; line-height: 18px; color: var(--text-muted);
  }
  .analysis-form { position: absolute; left: 60px; top: 150px; width: 291px; }
  .analysis-form__row { display: flex; gap: 12px; margin-bottom: 11px; }
  .analysis-form__field {
    flex: 1; height: 29px; background: var(--field-bg); padding: 0 10px;
    display: flex; align-items: center; font-size: 13px; font-weight: 300; color: var(--field-placeholder);
  }
  .analysis-form__field--email { flex: 0 0 143px; }
  .analysis-form__actions { display: flex; justify-content: flex-end; align-items: center; gap: 12px; margin-top: 1px; }
  .analysis-form__decline { font-style: italic; font-size: 13px; color: var(--text-muted); }
  .analysis-form__submit {
    width: 78px; height: 28px; background: var(--button-grey); color: var(--text-white);
    font-weight: 700; font-size: 13px; letter-spacing: 0.5px; display: flex; align-items: center; justify-content: center;
  }
</style>
</head>
<body>
<div class="canvas">
  <div class="site" aria-hidden="true">
    <div class="hero-photo" role="img" aria-label="Slideshow photo of a Midwest listing home with trees, lawn and driveway"></div>
    <div class="hero-dots"><span></span><span class="is-active"></span><span></span></div>
    <div class="listing-search">
      <div class="listing-search__bar"></div>
      <div class="listing-search__link">Advanced search</div>
    </div>
    <aside class="side-panel">
      <div class="brand">MY QV HOME</div>
      <ul class="main-nav">
        <li>HOME</li>
        <li>ABOUT MY QV HOME</li>
        <li>DOWNLOADS</li>
        <li>CONTACT</li>
      </ul>
      <div class="site-footer">MY QV HOME REALTY · MIDWEST<br>ALL RIGHTS RESERVED</div>
    </aside>
  </div>
  <div class="dim"></div>

  <section class="analysis-popup" aria-labelledby="popup-title">
    <svg class="analysis-popup__close" viewBox="0 0 20 20" aria-label="Close">
      <path d="M3 3 L17 17 M17 3 L3 17" stroke="#ffffff" stroke-width="4" stroke-linecap="round"/>
    </svg>
    <h2 class="analysis-popup__title" id="popup-title">MY FREE MARKET ANALYSIS</h2>
    <p class="analysis-popup__intro">Fill up the form below for a free market analysis.</p>
    <div class="analysis-form">
      <div class="analysis-form__row"><div class="analysis-form__field">Full Name</div></div>
      <div class="analysis-form__row">
        <div class="analysis-form__field analysis-form__field--email">Email Address</div>
        <div class="analysis-form__field">Phone Number</div>
      </div>
      <div class="analysis-form__row"><div class="analysis-form__field">Address</div></div>
      <div class="analysis-form__actions">
        <span class="analysis-form__decline">No, thanks.</span>
        <span class="analysis-form__submit">SUBMIT</span>
      </div>
    </div>
  </section>
</div>
</body>
</html>
```